Business Card Design for a Lending Business (Hard Money loans)

We need a business card for our Real Estate Lending business. We do hard Money loans for real estate investors. We have an existing logo we like, see attached. I'd like the business card to mostly include the logo colors, but a bright color pop of some sort would be nice to see also. Card should include Logo, Company Name, Company Address, Employee Name, Cell Phone, Main Phone, Email, Website

Industry/Entity Type

Finance / Lending

Contact Information for Business Card

Logo, Company Name, Company Address, Employee Name, Cell Phone, Main Phone, Email, Website

Requirements
Nice to have
• I'd like the business card to mostly include the logo colors, but a bright color pop of some sort would be nice to see also.

```html
<!DOCTYPE html>
<html lang="en">
<head>
<meta charset="utf-8">
<title>Ridgeway Funding – Business Card</title>
<link href="https://fonts.googleapis.com/css2?family=Montserrat:wght@400;500;700&display=swap" rel="stylesheet">
<style>
  :root {
    --stage: #3a3a3a;
    --navy: #0d2a8a;
    --royal: #0a4fc4;
    --sky: #00b0e0;
    --ink: #1b1b2a;
    --paper: #ffffff;
  }
  * { box-sizing: border-box; margin: 0; padding: 0; }
  html, body { width: 1200px; height: 875px; overflow: hidden; }
  body {
    background: var(--stage);
    font-family: "Montserrat", sans-serif;
    position: relative;
  }
  .card {
    position: absolute;
    left: 320px;
    width: 560px;
    height: 320px;
    border-radius: 26px;
    overflow: hidden;
  }
  .card--back {
    top: 90px;
    background: radial-gradient(ellipse at 50% 40%, #0a9ee0 0%, var(--royal) 45%, var(--navy) 100%);
    display: flex;
    flex-direction: column;
    align-items: center;
    justify-content: center;
    gap: 14px;
  }
  .card--front {
    top: 465px;
    background: var(--paper);
    border: 2px solid var(--navy);
  }
  .brand {
    display: flex;
    align-items: center;
    gap: 12px;
  }
  .brand__dot {
    width: 18px; height: 18px; border-radius: 50%;
    background: var(--sky);
  }
  .brand__name {
    font-weight: 700;
    letter-spacing: 5px;
    text-transform: uppercase;
    white-space: nowrap;
  }
  .card--back .brand__name { color: var(--paper); font-size: 30px; }
  .brand__rule { height: 2px; background: var(--sky); }
  .card--back .brand__rule { width: 300px; }

  .front__info {
    position: absolute;
    left: 34px;
    top: 28px;
    width: 320px;
  }
  .card--front .brand__name { color: var(--navy); font-size: 21px; letter-spacing: 3px; }
  .card--front .brand__rule { width: 280px; margin: 10px 0 18px; }
  .person__name { color: var(--navy); font-weight: 700; font-size: 19px; letter-spacing: 1px; }
  .person__role { color: var(--ink); font-size: 12px; letter-spacing: 1px; margin: 2px 0 12px; }
  .contact { list-style: none; font-size: 13px; color: var(--ink); line-height: 1.5; }
  .contact li { display: flex; align-items: center; gap: 8px; }
  .contact svg { width: 12px; height: 12px; fill: var(--sky); flex: none; }
  .contact .address { padding-left: 20px; }
  .front__mark {
    position: absolute;
    right: -40px;
    top: 30px;
    width: 240px;
    height: 240px;
    border-radius: 50%;
    background: var(--navy);
  }
</style>
</head>
<body>
  <section class="card card--back">
    <div class="brand">
      <span class="brand__dot"></span>
      <span class="brand__name">Ridgeway Funding</span>
    </div>
    <div class="brand__rule"></div>
  </section>

  <section class="card card--front">
    <div class="front__info">
      <div class="brand"><span class="brand__name">Ridgeway Funding</span></div>
      <div class="brand__rule"></div>
      <p class="person__name">MARCUS HALE</p>
      <p class="person__role">MANAGING DIRECTOR</p>
      <ul class="contact">
        <li><svg viewBox="0 0 12 12"><rect x="3" y="0" width="6" height="12" rx="1.5"/></svg>044-555 010 220</li>
        <li><svg viewBox="0 0 12 12"><path d="M2 1h3l1 3-2 1a7 7 0 0 0 3 3l1-2 3 1v3a1 1 0 0 1-1 1A10 10 0 0 1 1 2a1 1 0 0 1 1-1z"/></svg>044-555 010 221</li>
        <li><svg viewBox="0 0 12 12"><path d="M0 2h12v8H0z M0 2l6 4 6-4" /></svg>info@ridgewayfunding.com</li>
        <li><svg viewBox="0 0 12 12"><circle cx="6" cy="6" r="6"/></svg>www.ridgewayfunding.com</li>
        <li class="address">218 Harbor Point Drive</li>
        <li class="address">60614, United States</li>
      </ul>
    </div>
    <div class="front__mark"></div>
  </section>
</body>
</html>
```